Various Designs

We need various designs for our new hand disinfectant dispensers that feature three extra-large windows that allow users to customize the appearance simply by changing the graphics.
Each dispenser has one window at the front and one on each side. The front window can have two different sizes. Please refer to attached zip file named Dispenser_Design_Templates.
The designs should be fresh and of high quality. Please don't just place a photo and spam me.
The design should also contain our logo (TRL Switzerland - is included in the template).
The design should further be professional enough for a medical and public setting. The dispensers will be used in hospitals, medical facilities, old pension homes, schools, restaurants, kitchens, public places etc.
We value creativity a lot!
It would be great if the dispenser features a slogan such as "Hand Hygiene Saves Lives". I have added a number of slogans at the end of this description.
Do not use dark colors such as brown. These colors do not stand for hygiene. You can use black but only in conjunction with a bright color.
The following files contain designs that I like:
- 01w
- brivandecor
- worldwide
- IMG_0137
Slogans:
- Hand Hygiene Saves Lives
- Did you wash your hands?
- Did you disinfect your hands?
- Protect Yourself and Your Patients
- Healthy Hands Start Here
- Hand Hygiene We Love... We Care... We Share...
- Clean hands prevent germs from spreading.
- Practice Good Hand Hygiene
- Save Lives: Clean Your Hands
- Save Lives: Disinfect Your Hands
- Washing Hands Saves Lives
- Wash Your Hands Please
- Be aware…..!!!!! Wash with care…..!!!!!
- Hand Hygiene Station
- Hand Hygiene Share your care, not your germs
- Good Hand Hygiene It's Critical Sanitize Wash Moisturize
- Disinfect (image of a hand)
- Clean (image of a hand)
- No Water? No Problem. Waterless Hand Rub. Keep it Handy.
- Wash your hands! If not for yourself, then do it for them.
- Practice good hygiene - it-s contagious!
- Be aware, wash with care!
- Filthy fingers forecast sickness and sadness.
- Hand Hygiene The power is in your hands
- Bury the germ, Wash your hands
- Sanitize your hands and support our clean hands initiative
- Sanitize your hands. Together we can make a difference.
- You are grand if you wash your hand.
- Holding hands feels better when they’re clean.
- Be wise wash hands often.
- Wash those germs away!!!
- Your Hands Can Be Dangerous. Disinfect them to keep germs away.
- Ten out of ten patients prefer care from clean hands.
- Safety first, disinfect and protect
- It’s universal- handwashing every patient every time!
- Infection control is in your hands.
- Make your intention prevention. Wash your hands

```html
<!DOCTYPE html>
<html lang="en">
<head>
<meta charset="utf-8">
<title>TRL Switzerland – Healthy Hands Start Here</title>
<link href="https://fonts.googleapis.com/css2?family=Passion+One:wght@400;700&display=swap" rel="stylesheet">
<style>
  :root {
    --backdrop: #f2f2f2;
    --leaf-light: #8fd47e;
    --leaf-mid: #6cc163;
    --leaf-deep: #4f9e45;
    --headline: #ffffff;
    --headline-accent: #f1d4ae;
    --guide-line: #f3eb5e;
  }
  html, body {
    margin: 0;
    padding: 0;
    width: 1200px;
    height: 1000px;
    overflow: hidden;
    background: var(--backdrop);
  }
  .canvas {
    position: relative;
    width: 1200px;
    height: 1000px;
  }
  .window-graphic {
    position: absolute;
    left: 418px;
    top: 86px;
    width: 363px;
    height: 827px;
    clip-path: polygon(0 0, 100% 0, 84.8% 100%, 15.2% 100%);
    box-shadow: 0 0 20px rgba(0,0,0,0.15);
  }
  .vine-artwork {
    position: absolute;
    inset: 0;
    background:
      radial-gradient(ellipse at 60% 45%, var(--leaf-light) 0%, rgba(143,212,126,0) 60%),
      linear-gradient(160deg, var(--leaf-deep) 0%, var(--leaf-mid) 40%, var(--leaf-light) 70%, var(--leaf-mid) 100%);
  }
  .brand-name {
    position: absolute;
    left: 80px;
    top: 44px;
    margin: 0;
    font-family: "Passion One", sans-serif;
    font-weight: 400;
    font-size: 30px;
    line-height: 1;
    color: var(--headline);
    letter-spacing: 1px;
  }
  .slogan {
    margin: 0;
    font-family: "Passion One", sans-serif;
    font-weight: 700;
  }
  .slogan-line {
    position: absolute;
    display: block;
    font-size: 70px;
    line-height: 1;
    color: var(--headline);
    white-space: nowrap;
  }
  .slogan-line.healthy { left: 52px; top: 138px; }
  .slogan-line.hands { left: 78px; top: 192px; color: var(--headline-accent); }
  .slogan-line.start { left: 45px; top: 243px; }
  .slogan-line.here { left: 113px; top: 293px; }
  .guide-arrow {
    position: absolute;
    inset: 0;
    width: 363px;
    height: 827px;
  }
</style>
</head>
<body>
<main class="canvas">
  <section class="window-graphic">
    <div class="vine-artwork" role="img" aria-label="Illustration of green vines with leaves and a small bird perched on a branch"></div>
    <p class="brand-name">TRL Switzerland</p>
    <h1 class="slogan">
      <span class="slogan-line healthy">HEALTHY</span>
      <span class="slogan-line hands">HANDS</span>
      <span class="slogan-line start">START</span>
      <span class="slogan-line here">HERE</span>
    </h1>
    <svg class="guide-arrow" viewBox="0 0 363 827" aria-hidden="true">
      <path d="M 235 274 H 288 Q 300 274 300 286 V 345 Q 300 378 268 378 H 220 Q 208 378 208 390 V 800"
            fill="none" stroke="var(--guide-line)" stroke-width="9" stroke-linejoin="round"/>
      <path d="M 158 758 L 208 800 L 252 758"
            fill="none" stroke="var(--guide-line)" stroke-width="9"/>
    </svg>
  </section>
</main>
</body>
</html>
```